RP-Steuerberatung WordPress Site fully implemented (tax advisor)

Hello!
I need a little Wordpress Site for my newly founded Tax-Advisor Company.
I am a one-man Office advising in the area of Crypto-Currency.
PLEASE only provide a Design, if you can also Implement a WP-Site afterwards on an existing Webspace.

Please find the Content and Website-Description in the attached Document

Language for the Website is German (for now)

Target Market(s)

Tax-Advisory (specialized in Crypto Currency)

Coding

Coded - Design and coding required

Number of Pages Required

5+ page

Font styles to use
Sans Serif

Requirements
Must have
• Wordpress Implementation afterwards - Details according to attached Project Information Document

```html
<!DOCTYPE html>
<html lang="de">
<head>
<meta charset="utf-8">
<title>RP Steuerberatung – Leistungen</title>
<link href="https://fonts.googleapis.com/css2?family=Inter:wght@400;500;600;700&display=swap" rel="stylesheet">
<style>
:root{
  --navy:#1d2942;
  --ink:#1a1d24;
  --topbar:#1d2942;
  --cta:#0e2d6a;
  --footer:#282b33;
  --white:#ffffff;
  --muted:#c9ccd4;
  --accent-a:#0c2f6e;
  --accent-b:#1660c9;
}
*{box-sizing:border-box;margin:0;padding:0}
html,body{width:862px;height:1200px;overflow:hidden}
body{font-family:'Inter',sans-serif;color:var(--ink);background:var(--white);position:relative}
.wrap{width:711px;margin:0 auto;position:relative}

.topbar{height:26px;background:var(--topbar);color:var(--white);font-size:7.5px}
.topbar .wrap{display:flex;align-items:center;justify-content:space-between;height:100%}
.social{display:flex;gap:11px}
.social span{width:11px;height:11px;border:1.5px solid var(--white);border-radius:3px;display:block}
.contact-line{display:flex;gap:24px;align-items:center}
.contact-line div{display:flex;align-items:center;gap:5px}

.header{height:74px}
.header .wrap{display:flex;align-items:center;justify-content:space-between;height:100%}
.brand{display:flex;align-items:center;gap:8px;font-weight:700;font-size:15px;color:var(--navy);letter-spacing:.3px}
.brand-mark{width:30px;height:30px;background:var(--navy)}
.nav{display:flex;gap:17px;font-weight:600;font-size:10.5px;color:var(--ink)}
.nav .active{color:var(--navy);border-bottom:1.5px solid var(--navy);padding-bottom:3px}

.hero{height:227px;background:radial-gradient(ellipse at 75% 40%,#2a4a9c 0%,#152c68 40%,#050b1f 100%),linear-gradient(90deg,#0d3a8a,#050d24);display:flex;align-items:center;justify-content:center}
.hero h1{color:var(--white);font-size:43px;font-weight:600;margin-top:-4px}

.intro{width:640px;margin:48px auto 0;text-align:center;font-size:16px;line-height:23px}

.cards{position:absolute;top:500px;left:63px;display:grid;grid-template-columns:repeat(3,233px);column-gap:15px;row-gap:20px}
.card{height:127px;background:var(--white);border-radius:8px;box-shadow:0 6px 16px rgba(70,70,140,.14);display:flex;align-items:center;padding:0 12px 0 24px;gap:14px;font-size:13px;line-height:15.3px}
.card .tick{flex:0 0 19px;width:19px;height:19px;align-self:center}
.card.featured{background:linear-gradient(180deg,var(--accent-a),var(--accent-b));color:var(--white)}

.outro{position:absolute;top:826px;left:0;width:862px;text-align:center;font-size:16px;line-height:23px}

.cta{position:absolute;top:955px;left:0;width:862px;height:122px;background:var(--cta);color:var(--white);display:flex;align-items:center;justify-content:center;gap:10px;font-size:18px;font-weight:600}

.footer{position:absolute;top:1077px;left:0;width:862px;height:123px;background:var(--footer);color:var(--white)}
.footer-row{display:flex;align-items:center;height:85px;padding:0 8px}
.footer .brand{color:var(--white);font-size:12px;width:210px}
.footer .brand-mark{width:24px;height:24px;background:var(--white)}
.footer-contact{font-size:9px;line-height:11px;font-weight:500;width:200px}
.footer-nav{display:flex;gap:14px;font-size:9px;font-weight:500;margin-left:auto}
.footer hr{border:0;border-top:1px solid #5a5e68;width:711px;margin:0 auto}
.copyright{text-align:center;font-size:7.5px;font-weight:500;margin-top:9px}
</style>
</head>
<body>
<div class="topbar">
  <div class="wrap">
    <div class="social" aria-label="Soziale Netzwerke"><span></span><span></span></div>
    <div class="contact-line">
      <div>
        <svg width="9" height="9" viewBox="0 0 24 24"><path fill="#fff" d="M6.6 10.8a15 15 0 0 0 6.6 6.6l2.2-2.2a1 1 0 0 1 1-.25 11.4 11.4 0 0 0 3.6.57 1 1 0 0 1 1 1V20a1 1 0 0 1-1 1A17 17 0 0 1 3 4a1 1 0 0 1 1-1h3.5a1 1 0 0 1 1 1c0 1.25.2 2.45.57 3.57a1 1 0 0 1-.25 1z"/></svg>
        +43 512 000 481
      </div>
      <div>
        <svg width="11" height="8" viewBox="0 0 22 16"><rect width="22" height="16" rx="2" fill="#fff"/><path d="M1 1l10 8 10-8" stroke="#1d2942" stroke-width="2" fill="none"/></svg>
        office@rp-steuer.example
      </div>
    </div>
  </div>
</div>

<header class="header">
  <div class="wrap">
    <div class="brand"><span class="brand-mark"></span>RP STEUERBERATUNG</div>
    <nav class="nav">
      <span class="active">HOME</span><span>LEISTUNGEN</span><span>ÜBER MICH</span><span>KONTAKT</span><span>IMPRESSUM</span>
    </nav>
  </div>
</header>

<section class="hero" role="img" aria-label="Dunkelblaues Netzwerk aus verbundenen Knotenpunkten">
  <h1>Leistungen</h1>
</section>

<p class="intro">Ich biete in meiner Kanzlei ausschließlich Spezialberatung rund um die komplexen und vielseitigen Themen im Krypto-Bereich sowie deren Besteuerung, bzw. der Besteuerung und steuerlichen Optimierung von anderen passiven Einkommensmodellen an:</p>

<div class="cards">
  <div class="card"><svg class="tick" viewBox="0 0 20 20"><circle cx="10" cy="10" r="10" fill="#1d2942"/><path d="M5.5 10.3l3 3 6-6.3" stroke="#fff" stroke-width="2" fill="none"/></svg><p>Steueroptimales Besitzen von KryptoAssets auf in- und ausländischen Börsen</p></div>
  <div class="card featured"><svg class="tick" viewBox="0 0 20 20"><circle cx="10" cy="10" r="10" fill="#fff"/><path d="M5.5 10.3l3 3 6-6.3" stroke="#1551b8" stroke-width="2" fill="none"/></svg><p>Hilfestellung bei der Dokumentation der Einkünfte (Verwendung von Tax-Tools und Aufbereitung der Daten, etc.)</p></div>
  <div class="card"><svg class="tick" viewBox="0 0 20 20"><circle cx="10" cy="10" r="10" fill="#1d2942"/><path d="M5.5 10.3l3 3 6-6.3" stroke="#fff" stroke-width="2" fill="none"/></svg><p>Finanzstrafrechtliche Offenlegung und Aufarbeitung bei Einkünften die nicht ordnungsgemäß erklärt wurden.</p></div>
  <div class="card"><svg class="tick" viewBox="0 0 20 20"><circle cx="10" cy="10" r="10" fill="#1d2942"/><path d="M5.5 10.3l3 3 6-6.3" stroke="#fff" stroke-width="2" fill="none"/></svg><p>Beratung rund um das Thema Wegzug, Wohnsitzverlegung und in-/ausländische Gesellschaften.</p></div>
  <div class="card"><svg class="tick" viewBox="0 0 20 20"><circle cx="10" cy="10" r="10" fill="#1d2942"/><path d="M5.5 10.3l3 3 6-6.3" stroke="#fff" stroke-width="2" fill="none"/></svg><p>Hilfe bei der korrekten Erklärung der Crypto-Einkünfte und Erstellung der Steuererklärungen.</p></div>
  <div class="card"><svg class="tick" viewBox="0 0 20 20"><circle cx="10" cy="10" r="10" fill="#1d2942"/><path d="M5.5 10.3l3 3 6-6.3" stroke="#fff" stroke-width="2" fill="none"/></svg><p>Beratung bei der Unterscheidung und Besteuerung der diversen Einkunftsmöglichkeiten (Trading, Staking, Lending, Mining, Nodes, NFTs, , etc.)</p></div>
</div>

<p class="outro">Werden neben der Spezialberatung auch noch klassische Services wie<br>Buchhaltung, Lohnverrechnung etc. benötigt, kann dies gerne über<br>Partner-Kanzleien von mir organisiert werden.</p>

<section class="cta">
  nehmen sie gerne Kontakt mit mir auf!
  <svg width="12" height="12" viewBox="0 0 12 12"><path d="M1 6h10M7 2l4 4-4 4" stroke="#fff" stroke-width="1.2" fill="none"/></svg>
</section>

<footer class="footer">
  <div class="wrap">
    <div class="footer-row">
      <div class="brand"><span class="brand-mark"></span>RP STEUERBERATUNG</div>
      <div class="footer-contact">Email: office@rp-steuer.example<br>Phone : +43 512 000 481</div>
      <nav class="footer-nav"><span>HOME</span><span>LEISTUNGEN</span><span>ÜBER MICH</span><span>KONTAKT</span><span>IMPRESSUM</span></nav>
    </div>
  </div>
  <hr>
  <p class="copyright">Copyright © 2022 RP STEUERBERATUNG</p>
</footer>
</body>
</html>
```